the cobalt heron

I need a direct mail post card made for potential clients to pick up the phone and call us to order

Industry/Entity Type

Call

Font styles to use
Serif

Requirements
Must have
• Photos of the coin we are selling
• an attention grabbing headline
• a strong call to action, (MUST call now!)
• The price of the coin must be included
• A classic high dollar luxury feel to the post card mailer

```html
<!DOCTYPE html>
<html lang="en">
<head>
<meta charset="utf-8">
<title>The Cobalt Heron – Postcard</title>
<link rel="stylesheet" href="https://fonts.googleapis.com/css2?family=Roboto+Condensed:wght@200&family=Oswald:wght@700&family=Lato:wght@700;900&display=swap">
<style>
  :root {
    --ink: #000000;
    --paper: #ffffff;
    --gold-deep: #8a6220;
    --gold-mid: #b88a32;
    --gold-bright: #f8e07a;
    --gold-pale: #ffe98a;
    --silver: #cfcfd2;
    --price-ink: #1c1c1c;
  }
  * { margin: 0; padding: 0; box-sizing: border-box; }
  html, body {
    width: 1200px;
    height: 902px;
    overflow: hidden;
    background: var(--ink);
  }
  .postcard {
    position: relative;
    width: 1200px;
    height: 902px;
    background: var(--ink);
    overflow: hidden;
  }
  .headline {
    position: absolute;
    left: 90px;
    width: 772px;
    text-align: center;
    line-height: 1;
    white-space: nowrap;
    z-index: 2;
  }
  .headline-top {
    top: 64px;
    font-family: "Roboto Condensed", "Arial Narrow", sans-serif;
    font-weight: 200;
    font-size: 110px;
    color: var(--paper);
    letter-spacing: 0;
  }
  .headline-name {
    top: 182px;
    font-family: "Oswald", "Arial Narrow", sans-serif;
    font-weight: 700;
    font-size: 94px;
    letter-spacing: 1px;
    background: linear-gradient(180deg, var(--gold-pale) 0%, var(--gold-mid) 55%, var(--gold-deep) 100%);
    -webkit-background-clip: text;
    background-clip: text;
    color: transparent;
  }
  .coin-photo {
    position: absolute;
    top: 314px;
    width: 358px;
    height: 284px;
    border: 2px solid var(--paper);
    background: radial-gradient(circle at 50% 50%, #e6e6e8 0%, #a9a9ad 30%, #4a4a4d 44%, #0d0d0d 48%, #000 100%);
  }
  .coin-photo.reverse { left: 93px; }
  .coin-photo.obverse {
    left: 484px;
    background: radial-gradient(circle at 48% 48%, #bfc0c4 0%, #8e9095 32%, #3a3b3e 47%, #1a1a1a 54%, #0a0a0a 100%);
  }
  .price-tag {
    position: absolute;
    top: 598px;
    width: 290px;
    height: 46px;
    display: flex;
    align-items: center;
    justify-content: center;
    font-family: "Lato", sans-serif;
    font-weight: 900;
    font-size: 30px;
    color: var(--price-ink);
    background: linear-gradient(90deg, rgba(255,255,255,0) 0%, var(--silver) 25%, var(--paper) 50%, var(--silver) 75%, rgba(255,255,255,0) 100%);
  }
  .price-tag.reverse { left: 127px; }
  .price-tag.obverse { left: 518px; }
  .call-band {
    position: absolute;
    left: 0;
    top: 705px;
    width: 1200px;
    height: 125px;
    background: linear-gradient(90deg, var(--gold-deep) 0%, var(--gold-mid) 30%, var(--gold-bright) 58%, var(--gold-mid) 85%, var(--gold-deep) 100%);
  }
  .call-label {
    position: absolute;
    left: 68px;
    top: 42px;
    font-family: "Lato", sans-serif;
    font-weight: 700;
    font-size: 41px;
    line-height: 1;
    color: var(--paper);
  }
  .call-icon {
    position: absolute;
    left: 404px;
    top: 32px;
    width: 62px;
    height: 62px;
  }
  .call-number {
    position: absolute;
    left: 490px;
    top: 20px;
    font-family: "Oswald", "Arial Narrow", sans-serif;
    font-weight: 700;
    font-size: 72px;
    line-height: 1.15;
    color: var(--ink);
    letter-spacing: 1px;
  }
  .pattern-strip {
    position: absolute;
    left: 895px;
    top: 0;
    width: 253px;
    height: 902px;
    background: linear-gradient(180deg, #3a2a10 0%, #6b4d1c 30%, #8a6a2a 55%, #c9a449 78%, #6b4d1c 100%);
    opacity: 0.9;
  }
</style>
</head>
<body>
  <main class="postcard">
    <h1 class="headline headline-top">PURCHASE COIN</h1>
    <h2 class="headline headline-name">THE COBALT HERON</h2>

    <div class="coin-photo reverse" role="img" aria-label="Photo of the silver coin reverse showing a heraldic beast with a shield"></div>
    <div class="coin-photo obverse" role="img" aria-label="Photo of the silver coin obverse with the royal effigy"></div>

    <div class="price-tag reverse">$000</div>
    <div class="price-tag obverse">$000</div>

    <section class="call-band">
      <span class="call-label">Call us to order</span>
      <svg class="call-icon" viewBox="0 0 62 62" aria-hidden="true">
        <circle cx="31" cy="31" r="28" fill="none" stroke="#000" stroke-width="4"/>
        <path d="M22 17c1.5-1 3.2-.6 4 .8l2.6 4.6c.7 1.3.4 2.8-.7 3.7l-2 1.6c1.5 3.4 4.2 6.3 7.6 8l1.7-2c.9-1.1 2.5-1.4 3.7-.7l4.6 2.6c1.4.8 1.8 2.6.8 4l-1.9 2.7c-1.2 1.6-3.3 2.3-5.2 1.6C28.4 41.4 20.6 33.6 18 24.9c-.6-2 .1-4 1.7-5.2z" fill="#000"/>
      </svg>
      <span class="call-number">1234567890</span>
    </section>

    <div class="pattern-strip" role="img" aria-label="Decorative gold lace pattern strip"></div>
  </main>
</body>
</html>
```